Veterinary Practice

This is a large and small animal practice that primarily treats cattle,horses,dog and cats. I desire a business card with a picture of each of those animals. I prefer a black cow but the other animals can be any color. The back of the cards needs to have appointment scheduling information.

Industry/Entity Type

Business

Contact Information for Business Card

Copper Hollow Veterinary Services
Dennis M Palk DVM
3847 S Route 41
Larkfield KS 60418
555-319-2864

```html
<!DOCTYPE html>
<html lang="en">
<head>
<meta charset="utf-8">
<title>Copper Hollow Veterinary Services – Business Card</title>
<link rel="stylesheet" href="https://fonts.googleapis.com/css2?family=Lato:wght@400;700&display=swap">
<style>
  :root {
    --backdrop: #2a2a2a;
    --card: #f2f8f0;
    --green: #5db44b;
    --green-soft: #8cc97e;
    --ink: #1b1b1b;
    --line: #333333;
  }
  * { box-sizing: border-box; margin: 0; padding: 0; }
  html, body {
    width: 1200px; height: 900px; overflow: hidden;
    background: var(--backdrop);
    font-family: "Lato", Arial, sans-serif;
  }
  .stage {
    position: relative; width: 1200px; height: 900px;
    display: flex; flex-direction: column; align-items: center;
    justify-content: center; gap: 30px;
  }
  .card {
    position: relative; width: 700px; height: 400px;
    background: var(--card); overflow: hidden;
  }
  .edge-band {
    position: absolute; left: 0; right: 0; bottom: 0; height: 16px;
    background: var(--ink);
  }
  .edge-band__accent {
    position: absolute; bottom: 0; height: 16px; background: var(--green);
  }
  .card--front .edge-band__accent { left: 360px; width: 200px; }
  .card--back .edge-band { background: transparent; }
  .card--back .edge-band__accent { left: 380px; width: 280px; }

  .brand {
    position: absolute; left: 0; right: 0;
    display: flex; align-items: center; justify-content: center; gap: 14px;
  }
  .brand__dot {
    width: 56px; height: 56px; border-radius: 50%; background: var(--green);
    flex: none;
  }
  .brand__name {
    color: var(--green); font-weight: 700; font-size: 28px;
    letter-spacing: 0.3px; line-height: 1.1; white-space: nowrap;
  }

  .card--front .brand { top: 66px; }
  .contact {
    position: absolute; top: 180px; left: 0; right: 0; text-align: center;
  }
  .contact__name {
    color: var(--green); font-weight: 700; font-size: 26px; margin-bottom: 24px;
  }
  .contact__row { font-size: 19px; color: var(--ink); margin-bottom: 10px; }
  .contact__label { color: var(--green); font-weight: 700; }

  .card--back .brand { top: 36px; }
  .appointment { position: absolute; top: 120px; left: 110px; right: 110px; }
  .appointment__title {
    color: var(--green); font-size: 32px; font-weight: 400; text-align: center;
    border-top: 2px solid var(--green-soft); border-bottom: 2px solid var(--green-soft);
    padding: 6px 0 8px;
  }
  .field { display: flex; align-items: flex-end; gap: 10px; margin-top: 26px; }
  .field__label { font-size: 26px; color: var(--ink); white-space: nowrap; }
  .field__rule { flex: 1; border-bottom: 2px solid var(--line); margin-bottom: 7px; }
  .field--pet .field__label { color: var(--green); }
  .field--pet .field__rule { border-color: var(--green-soft); }
</style>
</head>
<body>
<main class="stage">
  <section class="card card--front" aria-label="Business card front">
    <div class="brand">
      <span class="brand__dot"></span>
      <span class="brand__name">Copper Hollow Veterinary Services, LLC</span>
    </div>
    <div class="contact">
      <p class="contact__name">Dennis M Palk DVM</p>
      <p class="contact__row"><span class="contact__label">Phone:</span> 555-319-2864</p>
      <p class="contact__row"><span class="contact__label">Address:</span> 3847 S Route 41 Larkfield KS 60418</p>
    </div>
    <div class="edge-band"><span class="edge-band__accent"></span></div>
  </section>

  <section class="card card--back" aria-label="Business card back">
    <div class="brand">
      <span class="brand__dot"></span>
      <span class="brand__name">Copper Hollow Veterinary Services</span>
    </div>
    <div class="appointment">
      <h2 class="appointment__title">Your Next Appointment</h2>
      <div class="field field--pet"><span class="field__label">Pet’s Name:</span><span class="field__rule"></span></div>
      <div class="field"><span class="field__label">Date:</span><span class="field__rule"></span></div>
      <div class="field"><span class="field__label">Time:</span><span class="field__rule"></span></div>
    </div>
    <div class="edge-band"><span class="edge-band__accent"></span></div>
  </section>
</main>
</body>
</html>
```